Maple Lantern Business Card

Design of business cards

Target Market(s)

We are aiming as small business owners who need anything from basic business structures, website plans, business processes and quality assurance.

Industry/Entity Type

Business

Colors

Designer to choose colors to be used in the design.

Requirements
Nice to have
• I would prefer one side of the card to use the green from the logo. Prefer to have the same font as the logo.

```html
<!DOCTYPE html>
<html lang="en">
<head>
<meta charset="utf-8">
<title>Maple Lantern Business Card</title>
<link rel="stylesheet" href="https://fonts.googleapis.com/css2?family=Gentium+Book+Plus:ital,wght@1,400&display=swap">
<style>
  :root {
    --brand-green: #a8cf3c;
    --card-white: #ffffff;
    --ink-grey: #58585a;
    --rule-grey: #4a4a4a;
  }
  html, body {
    margin: 0;
    padding: 0;
    overflow: hidden;
    background: var(--card-white);
  }
  .card {
    position: relative;
    width: 1200px;
    height: 741px;
    background: var(--card-white);
    overflow: hidden;
  }
  .band-top {
    position: absolute;
    left: 0;
    top: 0;
    width: 100%;
    height: 77px;
    background: var(--brand-green);
  }
  .band-bottom {
    position: absolute;
    left: 0;
    top: 502px;
    width: 100%;
    height: 239px;
    background: var(--brand-green);
  }
  .tagline-rule {
    position: absolute;
    left: 0;
    top: 452px;
    width: 410px;
    height: 2px;
    background: var(--rule-grey);
  }
  .tagline {
    position: absolute;
    left: 432px;
    top: 414px;
    margin: 0;
    font-family: "Gentium Book Plus", "Palatino Linotype", Palatino, serif;
    font-style: italic;
    font-weight: 400;
    font-size: 29px;
    line-height: 38px;
    color: var(--ink-grey);
    white-space: nowrap;
  }
</style>
</head>
<body>
  <div class="card">
    <div class="band-top"></div>
    <div class="tagline-rule"></div>
    <p class="tagline">basic business structures, website plans,<br>business processes &amp; quality assurance</p>
    <div class="band-bottom"></div>
  </div>
</body>
</html>
```